Label design for unique cold brew coffee product

Require a label for front and back of a clear glass flint flask bottle. This will hold our speciality cold brew coffee. the label is to have your logo and represent our brand of being rustic, industrial, funky, mechanical etc as per our attached logo.

look forward to seeing the funky cool designs that will help bring our awesome product to market.

Target Market(s)

Hipsters, coffee connoisseurs, and one that enjoys a fine coffee.

Industry/Entity Type

Cafe

Requirements
Must have
• Brand recognition, staying true to the essence of what we are about, producing fine speciality cold brew coffee. Must have an rustic, industrial, funky, mechanical feel to be aligned with the logo.
• Please ensure the following is included and is editable on the label:
• Ingredients: Specialty Coffee & Filtered Water
• Brewed on :
• Keep Refrigerated
• Facebook, instagram etc logo
• Volume: 200ml etc
• Website: www.kettlewharf.com.au
• Origin of the coffee
Should not have
• no bright colours

```html
<!DOCTYPE html>
<html lang="en">
<head>
<meta charset="utf-8">
<title>Kettle Wharf Cold Brew Labels</title>
<link rel="stylesheet" href="https://fonts.googleapis.com/css2?family=Saira+Semi+Condensed:wght@300;400;600;700&display=swap">
<style>
  :root{
    --stage:#e8e5e0;
    --panel-dark:#24170f;
    --rim:#7a2c20;
    --cream:#f4e8b9;
    --cream-soft:#efe3c4;
    --ink:#2a1c13;
    --bean:#7a3f1c;
    --gold:#d9a441;
    --dash:rgba(244,232,185,.6);
  }
  *{box-sizing:border-box;margin:0;padding:0}
  html,body{width:1200px;height:1026px;overflow:hidden;background:var(--stage)}
  body{font-family:"Saira Semi Condensed",sans-serif;position:relative}

  .label{position:absolute;top:150px;width:520px;height:720px}
  .label--front{left:45px}
  .label--back{left:635px}
  .label__shape{position:absolute;inset:0}

  .brand{position:absolute;left:0;right:0;text-align:center;color:var(--cream);font-weight:600;letter-spacing:4px;line-height:1}
  .brand__dot{display:inline-block;width:14px;height:14px;border-radius:50%;background:var(--gold);margin-right:12px;vertical-align:middle}
  .label--front .brand{top:155px;font-size:42px}
  .label--back .brand{top:108px;font-size:30px}

  .ribbon{position:absolute;left:50%;transform:translateX(-50%);background:var(--panel-dark);color:var(--cream);border:2px solid var(--cream-soft);border-radius:8px;font-weight:600;white-space:nowrap;text-align:center;line-height:1.3}
  .label--front .ribbon{top:235px;font-size:25px;padding:3px 34px}
  .label--back .ribbon{top:158px;font-size:18px;padding:2px 24px}

  .beans{position:absolute;border-radius:13px;background:linear-gradient(90deg,rgba(122,63,28,0) 0%,var(--bean) 20%,#9a5426 50%,var(--bean) 80%,rgba(122,63,28,0) 100%)}
  .label--front .beans{left:70px;width:380px;top:330px;height:26px}
  .label--back .beans{left:60px;width:230px;top:208px;height:16px}

  .rule{position:absolute;height:1px;background:rgba(244,232,185,.45)}
  .pill{position:absolute;background:var(--cream);color:var(--ink);border-radius:8px;text-align:center;font-weight:600;white-space:nowrap}

  .title{position:absolute;left:0;right:0;text-align:center;color:var(--cream);line-height:1}
  .title__cold{display:block;font-weight:700}
  .title__coffee{display:block;font-weight:300}
  .label--front .title{top:420px}
  .label--front .title__cold{font-size:70px}
  .label--front .title__coffee{font-size:80px;margin-top:6px}
  .label--back .title{top:510px}
  .label--back .title__cold{font-size:40px}
  .label--back .title__coffee{font-size:44px;margin-top:2px}

  .volume{position:absolute;right:34px;color:var(--cream);font-weight:300;font-size:18px;line-height:1}
  .label--front .volume{top:596px}
  .label--back .volume{top:596px}

  .info{position:absolute;left:80px;width:360px;top:242px;height:172px;border:1.5px dashed var(--dash);background:rgba(255,255,255,.08);color:var(--cream)}
  .info__head{text-align:center;font-weight:700;font-size:15px;color:var(--ink);padding-top:8px;line-height:1.2}
  .info__ingredients{text-align:center;font-weight:400;font-size:19px;padding:4px 0 10px;border-bottom:1.5px dashed var(--dash);line-height:1.2}
  .info__grid{display:grid;grid-template-columns:1fr 1fr;height:100px}
  .info__cell{font-weight:700;font-size:15px;color:var(--ink);padding-top:6px;line-height:1.2}
  .info__cell + .info__cell{border-left:1.5px dashed var(--dash);text-align:right}
  .info__cell span{display:block;border-bottom:1.5px dashed var(--dash);padding:0 24px 6px}

  .ornament{position:absolute;left:170px;top:632px}
</style>
</head>
<body>

<section class="label label--front">
  <svg class="label__shape" viewBox="0 0 520 720" width="520" height="720" aria-hidden="true">
    <defs>
      <radialGradient id="panelGlowFront" cx="50%" cy="35%" r="70%">
        <stop offset="0" stop-color="#6a4630"/>
        <stop offset="1" stop-color="#24170f"/>
      </radialGradient>
    </defs>
    <path d="M0,60 H190 L260,0 L330,60 H520 V640 H350 Q260,720 170,640 H0 Z" fill="none" stroke="var(--rim)" stroke-width="3"/>
    <rect x="14" y="72" width="492" height="560" fill="url(#panelGlowFront)"/>
  </svg>
  <div class="brand"><span class="brand__dot"></span>KETTLE WHARF</div>
  <div class="ribbon">Fine Speciality</div>
  <div class="beans" role="img" aria-label="Row of roasted coffee beans"></div>
  <div class="rule" style="left:70px;width:380px;top:380px"></div>
  <div class="pill" style="left:80px;width:220px;top:372px;height:14px"></div>
  <h1 class="title"><span class="title__cold">COLD BREW</span><span class="title__coffee">COFFEE</span></h1>
  <div class="rule" style="left:60px;width:340px;top:606px"></div>
  <div class="pill" style="left:125px;width:210px;top:598px;height:16px;font-size:12px;line-height:16px">www.kettlewharf.com.au</div>
  <div class="volume">200 ml</div>
  <svg class="ornament" width="180" height="72" viewBox="0 0 180 72" role="img" aria-label="Decorative brown swirl ornament">
    <ellipse cx="90" cy="36" rx="88" ry="34" fill="#fbf6ee" stroke="var(--rim)" stroke-width="2"/>
    <ellipse cx="90" cy="36" rx="60" ry="16" fill="#6b3d22" opacity=".55"/>
  </svg>
</section>

<section class="label label--back">
  <svg class="label__shape" viewBox="0 0 520 720" width="520" height="720" aria-hidden="true">
    <defs>
      <radialGradient id="panelGlowBack" cx="50%" cy="30%" r="75%">
        <stop offset="0" stop-color="#6a4630"/>
        <stop offset="1" stop-color="#24170f"/>
      </radialGradient>
    </defs>
    <path d="M0,60 H190 L260,0 L330,60 H520 V640 H350 Q260,720 170,640 H0 Z" fill="none" stroke="var(--rim)" stroke-width="3"/>
    <rect x="14" y="72" width="492" height="560" fill="url(#panelGlowBack)"/>
  </svg>
  <div class="brand"><span class="brand__dot"></span>KETTLE WHARF</div>
  <div class="ribbon">Fine Speciality</div>
  <div class="beans" role="img" aria-label="Row of roasted coffee beans"></div>
  <div class="rule" style="left:60px;width:400px;top:222px"></div>
  <div class="pill" style="left:155px;width:210px;top:212px;height:20px;font-size:14px;line-height:20px">www.kettlewharf.com.au</div>
  <div class="info">
    <div class="info__head">INGREDIENTS:</div>
    <div class="info__ingredients">Specialty Coffee &amp; Filtered Water</div>
    <div class="info__grid">
      <div class="info__cell"><span>BREWED ON:</span></div>
      <div class="info__cell"><span>ORIGIN:</span></div>
    </div>
  </div>
  <div class="pill" style="left:40px;width:440px;top:424px;height:17px;font-size:11px;line-height:17px;font-weight:400">KEEP REFRIGERATED</div>
  <div class="pill" style="left:40px;width:440px;top:448px;height:30px;font-size:14px;line-height:30px"><span style="font-weight:400">Find us on social media:</span> KETTLE WHARF</div>
  <div class="rule" style="left:40px;width:440px;top:494px"></div>
  <h2 class="title"><span class="title__cold">COLD BREW</span><span class="title__coffee">COFFEE</span></h2>
  <div class="volume">200 ml</div>
  <svg class="ornament" width="180" height="72" viewBox="0 0 180 72" role="img" aria-label="Decorative brown swirl ornament">
    <ellipse cx="90" cy="36" rx="88" ry="34" fill="#fbf6ee" stroke="var(--rim)" stroke-width="2"/>
    <ellipse cx="90" cy="36" rx="60" ry="16" fill="#6b3d22" opacity=".55"/>
  </svg>
</section>

</body>
</html>
```